Navigate the Underground Car Park to 7K3R Vet Clinic

Eye-catching signage for Underground Carpark.
We want to help new Clients, or those with bad senses of direction, to the correct Lift Lobby.
We want to be able to say 'Just follow the signs'.

It can be confusing and many other business have utilised some of the pillars in the carpark to guide their customers to the right place.

People don't want to walk far with sick animals so it is important they get to the right Lift Lobby.
Updates

We are thinking instead of 'Just Follow the Signs,We would like to try:'Looking for us?' (Large Text)'Follow the Signs (much smaller Text)Also, it is very useful to see the proposed sign dropped on to the photo of the car park pillars I included.Many thanks Added Friday, June 16, 2017

Target Market(s)

Customers, coming for the 1st time, trying to navigate the Underground CarPark towards the appropriate Lift lobby

Industry/Entity Type

Veterinary

Font styles to use
Serif

Colors
f78f20
00a990
0455a3

Requirements
Must have
• Logo.
• Bright. Clear. Not too cluttered.
• Warmth. Humour. Approachable.
• Please include: Building 4, Mezzanine Level
Nice to have
• Please look at our FB pages and Instagram page @7k3rvetclinic for a good feel of who we are.
• Some level of style or image continuity with the Pet Tips Poster (see attached file)
Should not have
• Not have a medical feel

```html
<!DOCTYPE html>
<html lang="en">
<head>
<meta charset="utf-8">
<title>7K3R Vet Clinic – Car Park Sign</title>
<link href="https://fonts.googleapis.com/css2?family=Open+Sans:wght@600;700;800&display=swap" rel="stylesheet">
<style>
  :root {
    --page: #c3cad6;
    --white: #ffffff;
    --teal: #14ab92;
    --teal-light: #6ab59e;
    --blue: #0455a3;
    --orange: #f78f20;
    --ink: #474747;
    --car-dark: #5b5b5b;
    --car-darker: #3f3f3f;
    --car-light: #ececec;
    --car-shade: #bdbdbd;
  }
  html, body {
    margin: 0;
    width: 1200px;
    height: 1200px;
    overflow: hidden;
    background: var(--page);
    font-family: "Open Sans", sans-serif;
  }
  .sign {
    position: absolute;
    left: 204px;
    top: 40px;
    width: 792px;
    height: 1120px;
    overflow: hidden;
    background: var(--teal);
    box-shadow: 0 10px 30px rgba(0,0,0,.18);
  }
  .sign__backdrop, .parking { position: absolute; left: 0; top: 0; }

  .sign__figure {
    position: absolute;
    left: 70px; top: 40px;
    width: 190px; height: 390px;
    border-radius: 90px 90px 30px 30px;
    background: linear-gradient(180deg, #b7835f 0%, #b7835f 18%, #3c3c3c 30%, #4a4a4a 62%, #5e5e5e 100%);
  }
  .sign__car-icon {
    position: absolute;
    left: 318px; top: 318px;
    width: 170px; height: 118px;
  }

  .brand {
    position: absolute;
    right: 48px; top: 168px;
    text-align: right;
  }
  .brand__name {
    display: flex; align-items: center; justify-content: flex-end; gap: 12px;
    margin: 0;
    color: var(--orange);
    font-weight: 800;
    font-size: 40px;
    line-height: 1;
    white-space: nowrap;
  }
  .brand__dot {
    width: 24px; height: 24px;
    border-radius: 50%;
    background: var(--teal);
    flex: none;
  }
  .brand__location {
    margin: 10px 0 0;
    color: var(--ink);
    font-weight: 600;
    font-size: 15px;
    letter-spacing: 3px;
    text-transform: uppercase;
    white-space: nowrap;
  }

  .headline {
    position: absolute;
    left: 0; right: 0; top: 440px;
    margin: 0;
    text-align: center;
    color: var(--blue);
    font-weight: 800;
    font-size: 88px;
    letter-spacing: -1px;
    line-height: 1;
    white-space: nowrap;
  }
  .subline {
    position: absolute;
    left: 0; right: 0; top: 548px;
    margin: 0;
    text-align: center;
    color: var(--ink);
    font-weight: 700;
    font-size: 36px;
    line-height: 1;
  }

  .parked-car {
    position: absolute;
    width: 210px; height: 96px;
    border-radius: 34px 24px 24px 34px;
    background: linear-gradient(90deg, var(--car-darker) 0%, var(--car-dark) 25%, #777 50%, var(--car-dark) 75%, var(--car-darker) 100%);
    box-shadow: 0 4px 8px rgba(0,0,0,.25);
  }
  .parked-car--light {
    background: linear-gradient(90deg, var(--car-shade) 0%, var(--car-light) 25%, #ffffff 50%, var(--car-light) 75%, var(--car-shade) 100%);
  }
  .bay-mark {
    position: absolute;
    width: 150px; height: 95px;
    border-radius: 48px 48px 12px 12px;
    background: rgba(255,255,255,.28);
  }
</style>
</head>
<body>
  <main class="sign">
    <svg class="sign__backdrop" width="792" height="1120" viewBox="0 0 792 1120" aria-hidden="true">
      <rect width="792" height="1120" fill="#14ab92"/>
      <polygon points="0,260 792,235 792,510 400,760 0,510" fill="#6ab59e"/>
      <polygon points="0,0 792,0 792,235 0,260" fill="#ffffff"/>
    </svg>

    <div class="sign__figure" role="img" aria-label="Illustration of a smiling man in a suit looking through a telescope"></div>

    <svg class="sign__car-icon" viewBox="0 0 170 118" aria-hidden="true">
      <g fill="#0455a3">
        <path d="M38 10 Q42 2 52 2 H118 Q128 2 132 10 L148 44 H22 Z"/>
        <rect x="4" y="40" width="24" height="12" rx="5"/>
        <rect x="142" y="40" width="24" height="12" rx="5"/>
        <path d="M12 52 Q14 42 30 42 H140 Q156 42 158 52 L162 88 Q162 96 154 96 H16 Q8 96 8 88 Z"/>
        <rect x="16" y="90" width="30" height="26" rx="6"/>
        <rect x="124" y="90" width="30" height="26" rx="6"/>
      </g>
      <path d="M46 12 H124 L136 40 H34 Z" fill="#6ab59e"/>
      <g fill="#6ab59e">
        <path d="M20 58 L50 62 L46 72 L22 68 Z"/>
        <path d="M150 58 L120 62 L124 72 L148 68 Z"/>
        <rect x="56" y="66" width="58" height="18" rx="4"/>
      </g>
      <g stroke="#0455a3" stroke-width="2.5">
        <line x1="64" y1="68" x2="64" y2="82"/><line x1="71" y1="68" x2="71" y2="82"/>
        <line x1="78" y1="68" x2="78" y2="82"/><line x1="85" y1="68" x2="85" y2="82"/>
        <line x1="92" y1="68" x2="92" y2="82"/><line x1="99" y1="68" x2="99" y2="82"/>
        <line x1="106" y1="68" x2="106" y2="82"/>
      </g>
    </svg>

    <div class="brand">
      <p class="brand__name"><span class="brand__dot"></span>7K3R Vet Clinic</p>
      <p class="brand__location">Building 4, Mezzanine Level</p>
    </div>

    <h1 class="headline">Looking for us?</h1>
    <p class="subline">Follow the Signs!</p>

    <svg class="parking" width="792" height="1120" viewBox="0 0 792 1120" aria-hidden="true">
      <g stroke="#ffffff" stroke-width="9" fill="none">
        <line x1="400" y1="625" x2="400" y2="1120"/>
        <line x1="90" y1="625" x2="700" y2="625"/>
        <line x1="90" y1="605" x2="90" y2="645"/>
        <line x1="700" y1="605" x2="700" y2="645"/>
        <line x1="80" y1="780" x2="700" y2="780"/>
        <line x1="80" y1="760" x2="80" y2="800"/>
        <line x1="700" y1="760" x2="700" y2="800"/>
        <line x1="70" y1="935" x2="690" y2="935"/>
        <line x1="70" y1="915" x2="70" y2="955"/>
        <line x1="690" y1="915" x2="690" y2="955"/>
      </g>
    </svg>

    <div class="parked-car" style="left:130px; top:655px;" role="img" aria-label="Top view of a dark grey parked car"></div>
    <div class="parked-car" style="left:445px; top:655px;" role="img" aria-label="Top view of a dark grey parked car"></div>
    <div class="parked-car parked-car--light" style="left:445px; top:810px;" role="img" aria-label="Top view of a white parked car"></div>
    <div class="parked-car" style="left:440px; top:975px;" role="img" aria-label="Top view of a dark grey parked car with headlights on"></div>
    <div class="bay-mark" style="left:160px; top:810px;" role="img" aria-label="White line pictogram painted on an empty parking bay"></div>
    <div class="bay-mark" style="left:150px; top:975px;" role="img" aria-label="White line pictogram painted on an empty parking bay"></div>
  </main>
</body>
</html>
```